Business Card *

A business card design
Use the logo uploaded in the brief page.
You may use placeholders in your design layouts.
I will provide the actual business card details to the winning designer.

Logo
Place for contact info (name, title, phone, email, etc)

Requirements
Must have
• Logo

```html
<!DOCTYPE html>
<html lang="en">
<head>
<meta charset="utf-8">
<title>Harlow Fields – Business Card Options</title>
<link href="https://fonts.googleapis.com/css2?family=Lato:wght@400;700;900&display=swap" rel="stylesheet">
<style>
  :root{
    --backdrop:#a8a8a8;
    --label:#2f2f2f;
    --charcoal:#2a2a2a;
    --gear:#5e5e5e;
    --white:#ffffff;
    --green-dark:#0b6a1f;
    --green-light:#82c51f;
    --ink:#3a3a3a;
    --grey-light:#cfcfcf;
    --grey-mid:#6e6e6e;
  }
  html,body{margin:0;padding:0;overflow:hidden;}
  body{width:907px;height:1200px;background:var(--backdrop);position:relative;font-family:"Lato",sans-serif;}
  .option{position:absolute;left:0;width:907px;height:600px;}
  .option--five{top:0;}
  .option--six{top:600px;}
  .card{position:absolute;width:380px;height:217px;box-shadow:0 6px 14px rgba(0,0,0,.25);}
  .card--front{left:185px;top:70px;}
  .card--back{left:340px;top:335px;}
  .option-label{position:absolute;left:56px;top:445px;margin:0;font-size:44px;font-weight:700;color:var(--label);}
  .card svg{display:block;}
  .holder-name{font-weight:900;font-size:24px;fill:var(--white);}
  .holder-title{font-size:9px;fill:var(--white);}
  .brand-small{font-weight:900;font-size:10px;fill:var(--green-dark);}
  .brand-large{font-weight:900;font-size:19px;fill:var(--white);}
  .contact{font-size:8px;fill:var(--ink);}
</style>
</head>
<body>

<svg width="0" height="0" style="position:absolute" aria-hidden="true">
  <defs>
    <linearGradient id="green-band" x1="0" y1="0" x2="1" y2="0">
      <stop offset="0" stop-color="var(--green-dark)"/>
      <stop offset="1" stop-color="var(--green-light)"/>
    </linearGradient>
    <linearGradient id="green-band-rev" x1="1" y1="0" x2="0" y2="0">
      <stop offset="0" stop-color="var(--green-dark)"/>
      <stop offset="1" stop-color="var(--green-light)"/>
    </linearGradient>
    <linearGradient id="steel" x1="0" y1="0" x2="1" y2="0">
      <stop offset="0" stop-color="#9a9a9a"/>
      <stop offset="1" stop-color="#4a4a4a"/>
    </linearGradient>
    <linearGradient id="steel-rev" x1="1" y1="0" x2="0" y2="0">
      <stop offset="0" stop-color="#9a9a9a"/>
      <stop offset="1" stop-color="#4a4a4a"/>
    </linearGradient>
    <radialGradient id="art-grey"><stop offset="0" stop-color="#8a8a8a"/><stop offset="1" stop-color="#e6e6e6"/></radialGradient>
    <radialGradient id="art-green"><stop offset="0" stop-color="#3aa84a"/><stop offset="1" stop-color="#d9efd6"/></radialGradient>
  </defs>
</svg>

<!-- OPTION 5 -->
<section class="option option--five">
  <div class="card card--front">
    <svg width="380" height="217" viewBox="0 0 380 217">
      <rect width="380" height="217" fill="var(--charcoal)"/>
      <polygon points="165,50 212,50 232,30 380,30 380,187 232,187 212,167 165,167" fill="url(#green-band)" stroke="var(--white)" stroke-width="4"/>
      <circle cx="92" cy="108" r="112" fill="var(--gear)"/>
      <circle cx="92" cy="108" r="96" fill="var(--white)"/>
      <rect x="0" y="0" width="92" height="217" fill="var(--white)"/>
      <text class="holder-name" x="238" y="110">John Doe</text>
      <text class="holder-title" x="318" y="126">Founder</text>
      <circle cx="62" cy="64" r="6" fill="var(--green-dark)"/>
      <text class="brand-small" x="72" y="68">HARLOW FIELDS</text>
      <line x1="55" y1="80" x2="140" y2="80" stroke="var(--ink)" stroke-dasharray="2 2" stroke-width=".8"/>
      <rect x="68" y="89" width="5" height="5" fill="var(--ink)"/><text class="contact" x="80" y="95">123-456-789</text>
      <rect x="68" y="103" width="6" height="4" fill="var(--ink)"/><text class="contact" x="80" y="108">email@website.com</text>
      <circle cx="71" cy="118" r="2.5" fill="var(--ink)"/><text class="contact" x="80" y="121">www.website.com</text>
      <circle cx="71" cy="131" r="2" fill="var(--ink)"/><text class="contact" x="80" y="134">Address Line 1,</text>
      <text class="contact" x="80" y="145">Address Line 2,</text>
      <text class="contact" x="80" y="156">City, State</text>
    </svg>
  </div>
  <div class="card card--back">
    <svg width="380" height="217" viewBox="0 0 380 217">
      <rect width="380" height="217" fill="var(--charcoal)"/>
      <polygon points="0,30 150,30 170,50 215,50 215,167 170,167 150,187 0,187" fill="url(#green-band-rev)" stroke="var(--white)" stroke-width="4"/>
      <circle cx="288" cy="108" r="112" fill="var(--gear)"/>
      <circle cx="288" cy="108" r="96" fill="var(--white)"/>
      <rect x="288" y="0" width="92" height="217" fill="var(--white)"/>
      <circle cx="300" cy="108" r="70" fill="url(#art-grey)" role="img" aria-label="Leaf illustration over field rows in grey"/>
      <circle cx="104" cy="90" r="10" fill="var(--white)"/>
      <text class="brand-large" x="40" y="132">HARLOW FIELDS</text>
    </svg>
  </div>
  <p class="option-label">option 5</p>
</section>

<!-- OPTION 6 -->
<section class="option option--six">
  <div class="card card--front">
    <svg width="380" height="217" viewBox="0 0 380 217">
      <rect width="380" height="217" fill="url(#steel)"/>
      <polygon points="165,50 212,50 232,30 380,30 380,187 232,187 212,167 165,167" fill="url(#green-band)" stroke="var(--white)" stroke-width="4"/>
      <circle cx="92" cy="108" r="112" fill="var(--gear)"/>
      <circle cx="92" cy="108" r="96" fill="var(--white)"/>
      <rect x="0" y="0" width="92" height="217" fill="var(--white)"/>
      <text class="holder-name" x="238" y="110">John Doe</text>
      <text class="holder-title" x="318" y="126">Founder</text>
      <circle cx="62" cy="64" r="6" fill="var(--green-dark)"/>
      <text class="brand-small" x="72" y="68">HARLOW FIELDS</text>
      <line x1="55" y1="80" x2="140" y2="80" stroke="var(--ink)" stroke-dasharray="2 2" stroke-width=".8"/>
      <rect x="68" y="89" width="5" height="5" fill="var(--ink)"/><text class="contact" x="80" y="95">123-456-789</text>
      <rect x="68" y="103" width="6" height="4" fill="var(--ink)"/><text class="contact" x="80" y="108">email@website.com</text>
      <circle cx="71" cy="118" r="2.5" fill="var(--ink)"/><text class="contact" x="80" y="121">www.website.com</text>
      <circle cx="71" cy="131" r="2" fill="var(--ink)"/><text class="contact" x="80" y="134">Address Line 1,</text>
      <text class="contact" x="80" y="145">Address Line 2,</text>
      <text class="contact" x="80" y="156">City, State</text>
    </svg>
  </div>
  <div class="card card--back">
    <svg width="380" height="217" viewBox="0 0 380 217">
      <rect width="380" height="217" fill="url(#steel-rev)"/>
      <polygon points="0,30 150,30 170,50 215,50 215,167 170,167 150,187 0,187" fill="url(#green-band-rev)" stroke="var(--white)" stroke-width="4"/>
      <circle cx="288" cy="108" r="112" fill="var(--gear)"/>
      <circle cx="288" cy="108" r="96" fill="var(--white)"/>
      <rect x="288" y="0" width="92" height="217" fill="var(--white)"/>
      <circle cx="300" cy="108" r="70" fill="url(#art-green)" role="img" aria-label="Leaf illustration over field rows in green"/>
      <circle cx="104" cy="90" r="10" fill="var(--white)"/>
      <text class="brand-large" x="40" y="132">HARLOW FIELDS</text>
    </svg>
  </div>
  <p class="option-label">option 6</p>
</section>

</body>
</html>
```